Four in One (Flexible infographic for Content Management Industry)

See attachment.
A graphic depicting 4 products, where each can stand on its own and each can be combined with others, but where, if all are taken together, the best result is achieved (the "super product").
Intended use is web. See attached file as an example.
The most basic idea is as the attached diagram shows, where 4 rectangles are arranged in a quadrangle, with a middle rectangle in the center representing the combined 4 products. This concept is fine except it is a bit too obvious as it stands. We are looking for either a variation of this or another concept.
The audience is technical + professional + enterprise - NOT consumers. Hence the design should be conservative in nature.
We are aware of tools like as Canva or Pictogram where such graphics are available, but we are looking for something with a bit more imagination and flexibility.
This graphic should be targeted to web sites and be delivered with vector-based (SVG) graphics.

```html
<!DOCTYPE html>
<html lang="en">
<head>
<meta charset="utf-8">
<title>Super Product – Four in One</title>
<link rel="stylesheet" href="https://fonts.googleapis.com/css2?family=Fira+Sans:wght@800&family=Montserrat:wght@600;800&family=Roboto:wght@500&display=swap">
<style>
  :root {
    --navy: #2e314b;
    --band: #e6e7e9;
    --paper: #ffffff;
    --edge: #e4e4e6;
  }
  html, body {
    margin: 0;
    width: 1200px;
    height: 1142px;
    overflow: hidden;
    background: var(--paper);
  }
  .canvas {
    position: relative;
    width: 1741px;
    height: 1656px;
    transform: scale(0.6893);
    transform-origin: 0 0;
    color: var(--navy);
  }
  .structure { position: absolute; inset: 0; }
  .heading {
    position: absolute;
    margin: 0;
    font-family: "Fira Sans", sans-serif;
    font-weight: 800;
    font-size: 42px;
    line-height: 1;
    white-space: nowrap;
  }
  .summary {
    position: absolute;
    margin: 0;
    font-family: "Montserrat", sans-serif;
    font-weight: 600;
    font-size: 25px;
    line-height: 34px;
    white-space: nowrap;
  }
  .summary--plain { font-family: "Roboto", sans-serif; font-weight: 500; font-size: 26px; }
  .features {
    position: absolute;
    margin: 0;
    padding: 0;
    list-style: none;
    font-family: "Montserrat", sans-serif;
    font-weight: 600;
    font-size: 25px;
    line-height: 30px;
    white-space: nowrap;
  }
  .features--plain { font-family: "Roboto", sans-serif; font-weight: 500; font-size: 26px; }
  .features--compact { font-size: 21px; line-height: 25px; }
  .features--ticked li { position: relative; }
  .features--ticked li svg {
    position: absolute;
    left: -27px;
    top: 50%;
    width: 16px;
    height: 14px;
    transform: translateY(-35%);
  }
  .product-title {
    position: absolute;
    left: 235px;
    width: 1295px;
    top: 768px;
    margin: 0;
    text-align: center;
    font-family: "Montserrat", sans-serif;
    font-weight: 800;
    font-size: 92px;
    line-height: 110px;
    color: var(--paper);
    letter-spacing: 1px;
  }
</style>
</head>
<body>
<main class="canvas">
  <svg class="structure" viewBox="0 0 1741 1656" width="1741" height="1656" aria-hidden="true">
    <rect x="1" y="1" width="1739" height="1654" fill="none" stroke="var(--edge)" stroke-width="2"/>
    <g fill="var(--navy)">
      <rect x="135" y="85" width="667" height="667"/>
      <rect x="938" y="85" width="667" height="667"/>
      <rect x="135" y="879" width="667" height="666"/>
      <rect x="938" y="879" width="667" height="666"/>
    </g>
    <g fill="var(--paper)">
      <rect x="171" y="121" width="596" height="596"/>
      <rect x="974" y="121" width="596" height="596"/>
      <rect x="171" y="914" width="596" height="596"/>
      <rect x="974" y="914" width="596" height="596"/>
    </g>
    <g fill="var(--band)">
      <rect x="171" y="208" width="596" height="85"/>
      <rect x="974" y="208" width="596" height="85"/>
      <rect x="171" y="1025" width="596" height="85"/>
      <rect x="974" y="1025" width="596" height="85"/>
    </g>
    <rect x="235" y="672" width="1295" height="300" fill="var(--navy)"/>
    <g fill="var(--paper)">
      <rect x="235" y="717" width="567" height="35"/>
      <rect x="938" y="717" width="567" height="35"/>
      <rect x="235" y="879" width="567" height="35"/>
      <rect x="938" y="879" width="567" height="35"/>
      <rect x="767" y="660" width="35" height="92"/>
      <rect x="938" y="660" width="36" height="92"/>
      <rect x="767" y="879" width="35" height="93"/>
      <rect x="938" y="879" width="36" height="93"/>
    </g>
  </svg>

  <section class="module module--documents">
    <h2 class="heading" style="left:201px; top:228px;">Document Management</h2>
    <p class="summary summary--plain" style="left:191px; top:313px;">Streamline document organization, access,<br>and collaboration with easier file storage and<br>sharing, leading to more efficient workflows .</p>
    <ul class="features features--plain features--ticked" style="left:219px; top:489px;">
      <li><svg viewBox="0 0 16 14"><path d="M1 7l5 5L15 1" fill="none" stroke="currentColor" stroke-width="3"/></svg>Centralized Document Control</li>
      <li><svg viewBox="0 0 16 14"><path d="M1 7l5 5L15 1" fill="none" stroke="currentColor" stroke-width="3"/></svg>Collaborative Workspace Integration</li>
      <li><svg viewBox="0 0 16 14"><path d="M1 7l5 5L15 1" fill="none" stroke="currentColor" stroke-width="3"/></svg>Automated Compliance Tracking</li>
      <li><svg viewBox="0 0 16 14"><path d="M1 7l5 5L15 1" fill="none" stroke="currentColor" stroke-width="3"/></svg>Check 4</li>
    </ul>
  </section>

  <section class="module module--security">
    <h2 class="heading" style="left:990px; top:228px;">Security and Compliance</h2>
    <p class="summary" style="left:1004px; top:313px;">Benefit from tailored cloud solutions,<br>secure data storage, and expert disaster<br>recovery planning for reliable and scalable</p>
    <ul class="features" style="left:1032px; top:489px;">
      <li>Custom Cloud Solutions</li>
      <li>Secure Data Storage</li>
      <li>Expert Disaster Recovery</li>
      <li>Check 4</li>
    </ul>
  </section>

  <h1 class="product-title">SUPER PRODUCT</h1>

  <section class="module module--erp">
    <h2 class="heading" style="left:182px; top:1047px; font-size:40px;">Enterprise&nbsp; Resource Planning</h2>
    <p class="summary" style="left:191px; top:1130px; line-height:33px;">Simplify management across finance, sales,<br>and operations, enabling better decision-<br>making and improved productivity.</p>
    <ul class="features features--compact features--ticked" style="left:219px; top:1306px;">
      <li><svg viewBox="0 0 16 14"><path d="M1 7l5 5L15 1" fill="none" stroke="currentColor" stroke-width="3"/></svg>Integrated Business Processes</li>
      <li><svg viewBox="0 0 16 14"><path d="M1 7l5 5L15 1" fill="none" stroke="currentColor" stroke-width="3"/></svg>Enhanced Decision-Making</li>
      <li><svg viewBox="0 0 16 14"><path d="M1 7l5 5L15 1" fill="none" stroke="currentColor" stroke-width="3"/></svg>Productivity Improvement</li>
      <li><svg viewBox="0 0 16 14"><path d="M1 7l5 5L15 1" fill="none" stroke="currentColor" stroke-width="3"/></svg>Check 4</li>
    </ul>
  </section>

  <section class="module module--digital">
    <h2 class="heading" style="left:1016px; top:1045px;">Digital Transformation</h2>
    <p class="summary" style="left:1004px; top:1130px; line-height:30px;">Turn scanned documents into easily<br>searchable digital archives, boosting<br>efficiency and accessibility.</p>
    <ul class="features" style="left:1032px; top:1306px;">
      <li>Instant searchable Archives with<br>OCR</li>
      <li>Automated Document<br>Classification</li>
      <li>Quillary and Cloud Blob</li>
    </ul>
  </section>
</main>
</body>
</html>
```